Kelvane Plumbing Business cards

Company is Kelvane Plumbing.
name Dashel Morrowby, I am a plumber, drainer, gasfitter and roofer
Mobile: 0431 906 154
Email address: info@kelvaneplumbing.example (check out my website for some ideas)
Website: www.kelvaneplumbing.example
ABN: 82 916 203 471
LIC: 604517K

I am reliable all round plumber. I am a 24 hour emergency service. Kelvane Plumbing is a professional plumbing service in the Illawarra, South Coast, Southern Sydney and Southern Highland regions of NSW. We offer a 24 hour emergency service for piece of mind to our customers. Call us now to see how we can help you. Kelvane Plumbing approaches every job with attention to detail and excellent customer service. With our superior workmanship you can be confident that the job will be done right the first time around. You can rest assured with results that are guaranteed to last.

Target Market(s)

the general public

Contact Information for Business Card

look up website for some ideas something with similar colours to logo and new modern and to catch the eye.

Colors
fdfdfd
ffffff
000000
7f7f7f
aaaaaa
33a6d7
0492cd

Requirements
Must have
• all contact details
• company- Kelvane Plumbing
• name- Dashel Morrowby
• number mobile- 0431 906 154
• Email address- info@kelvaneplumbing.example
• Website- www.kelvaneplumbing.example
• ABN- 82 916 203 471
• LIC- 604517K

```html
<!DOCTYPE html>
<html lang="en">
<head>
<meta charset="utf-8">
<title>Kelvane Plumbing – Business Cards</title>
<link href="https://fonts.googleapis.com/css2?family=Lato:wght@400;700;900&display=swap" rel="stylesheet">
<style>
  :root {
    --blue: #0492cd;
    --blue-light: #33a6d7;
    --grey: #7f7f7f;
    --grey-light: #aaaaaa;
    --ink: #000000;
    --paper: #ffffff;
    --stage: #e9ebee;
  }
  * { box-sizing: border-box; margin: 0; padding: 0; }
  html, body { width: 1200px; height: 782px; overflow: hidden; }
  body {
    background: var(--stage);
    font-family: 'Lato', sans-serif;
    display: flex;
    align-items: center;
    justify-content: center;
    gap: 40px;
  }
  .card {
    position: relative;
    width: 540px;
    height: 310px;
    background: var(--paper);
    box-shadow: 0 6px 18px rgba(0,0,0,.18);
    overflow: hidden;
  }
  .card__band { position: absolute; inset: 0; }
  .brand {
    position: absolute;
    left: 200px; top: 42px;
    width: 140px; height: 140px;
    border-radius: 50%;
    background: var(--paper);
    display: flex; align-items: center; justify-content: center;
    text-align: center;
  }
  .brand__name {
    color: var(--blue);
    font-weight: 900;
    font-size: 19px;
    line-height: 1.1;
    letter-spacing: .5px;
  }
  .services {
    position: absolute;
    left: 0; right: 0; top: 196px;
    text-align: center;
    font-size: 14px;
    line-height: 1.45;
    color: #222;
  }
  .services .dot {
    display: inline-block;
    width: 7px; height: 7px;
    border-radius: 50%;
    background: var(--blue);
    margin: 0 6px 2px;
  }
  .contact {
    position: absolute;
    left: 0; right: 0; top: 190px;
    text-align: center;
    color: #222;
  }
  .contact__name {
    color: var(--blue);
    font-weight: 900;
    font-size: 20px;
    letter-spacing: .5px;
  }
  .contact__role { font-size: 14px; margin-top: 1px; }
  .contact__rule {
    width: 330px; height: 1px;
    background: var(--grey-light);
    margin: 8px auto 7px;
  }
  .contact__line { font-size: 13.5px; line-height: 1.5; }
  .contact__label { color: var(--blue); }
  .contact__web .contact__accent { color: var(--blue); }
</style>
</head>
<body>

  <section class="card card--front" aria-label="Business card front">
    <svg class="card__band" width="540" height="310" viewBox="0 0 540 310">
      <polygon points="0,0 540,0 540,160 290,160 270,95 0,95" fill="var(--blue)"/>
    </svg>
    <div class="brand"><span class="brand__name">KELVANE<br>PLUMBING</span></div>
    <div class="services">
      <p>Blocked Drains<span class="dot"></span>CCTV Camera Inspections<span class="dot"></span>Emergency Services</p>
      <p>Burst Pipes &amp; Leaking Taps<span class="dot"></span>Hot Water Services</p>
      <p>Gasfitting<span class="dot"></span>Roofing, Guttering &amp; Downpipes</p>
      <p>Kitchens, Bathrooms &amp; Laundrys<span class="dot"></span>Rainwater Tanks</p>
    </div>
  </section>

  <section class="card card--back" aria-label="Business card back">
    <svg class="card__band" width="540" height="310" viewBox="0 0 540 310">
      <polygon points="0,0 540,0 540,160 290,160 270,95 0,95" fill="var(--grey)"/>
    </svg>
    <div class="brand"><span class="brand__name">KELVANE<br>PLUMBING</span></div>
    <div class="contact">
      <p class="contact__name">DASHEL MORROWBY</p>
      <p class="contact__role">Plumber, Drainer, Gasfitter, Roofer</p>
      <div class="contact__rule"></div>
      <p class="contact__line"><span class="contact__label">P:</span> 0431 906 154 | <span class="contact__label">E:</span> info@kelvaneplumbing.example</p>
      <p class="contact__line"><span class="contact__label">LIC:</span> 604517K | <span class="contact__label">ABN:</span> 82 916 203 471</p>
      <p class="contact__line contact__web">www.<span class="contact__accent">kelvaneplumbing</span>.example</p>
    </div>
  </section>

</body>
</html>
```